依頼概要
ゴルフクラブカスタムショップ『R7 Forge』で作成(チューニング)したクラブに貼るシールデザインをお願い致します。

こちらのシールは当店でチューニングしたゴルフクラブ全てに貼る調整済の証のシールです。あまり派手にすると嫌がられるお客様もいらっしゃる為、落ち着いた高級感のあるイメージでお願い致します。

●シールサイズ
縦2.8cm 横5.5cm
※端の3mmほど重なります。

●色
シールベース ゴールド

●文字色
ブラック
※ワンポイントカラーが入ってもOKです。

●文字内容
チューニング済みの証→『TUNING COMPLETED』
※文字体、大、小文字はお任せします。

店名→『R7 Forge』

イメージは写真を、ご参考下さい。
この写真のシールに似た雰囲気で高級感ある、良い意味で目立ち過ぎないシールにしたいです。

当店HP  http://www.r7forge-example.jp/

追記
今現在のr7forgeのホームページは水色がイメージカラーとなってますが、今後はこの色合いも変更していく予定となってますので、水色は意識して頂かなくて結構です。

```html
<!DOCTYPE html>
<html lang="en">
<head>
<meta charset="utf-8">
<title>R7 Forge — Tuning Completed Seal</title>
<link href="https://fonts.googleapis.com/css2?family=Oswald:wght@500&family=Montserrat:wght@600&display=swap" rel="stylesheet">
<style>
  :root {
    --backdrop: #8e8e8e;
    --gold-light: #e6c987;
    --gold-mid: #c9a457;
    --gold-deep: #a8833c;
    --panel: #2a1c12;
    --ink: #14100c;
  }
  * { margin: 0; padding: 0; box-sizing: border-box; }
  html, body {
    width: 841px;
    height: 1200px;
    overflow: hidden;
    background: var(--backdrop);
  }
  .seal {
    position: absolute;
    left: 140px;
    top: 50px;
    width: 560px;
    height: 1100px;
    background: linear-gradient(90deg, var(--gold-deep) 0%, var(--gold-light) 30%, var(--gold-mid) 60%, var(--gold-light) 80%, var(--gold-deep) 100%);
  }
  .certificate-panel {
    position: absolute;
    top: 30px;
    width: 200px;
    height: 740px;
    background: var(--panel);
    display: flex;
    justify-content: center;
    align-items: center;
  }
  .certificate-panel::before {
    content: "";
    position: absolute;
    inset: 14px;
    border: 3px solid var(--gold-mid);
  }
  .certificate-panel--left { left: 50px; }
  .certificate-panel--right { left: 310px; }
  .certificate-text {
    writing-mode: vertical-rl;
    font-family: "Montserrat", sans-serif;
    font-weight: 600;
    font-size: 50px;
    line-height: 1.5;
    letter-spacing: 12px;
    color: var(--gold-light);
    text-align: center;
  }
  .shop-name {
    position: absolute;
    left: 0;
    right: 0;
    top: 850px;
    text-align: center;
    font-family: "Oswald", sans-serif;
    font-weight: 500;
    font-size: 120px;
    letter-spacing: 8px;
    color: var(--ink);
  }
</style>
</head>
<body>
  <div class="seal">
    <div class="certificate-panel certificate-panel--left">
      <p class="certificate-text">TUNING<br>COMPLETED</p>
    </div>
    <div class="certificate-panel certificate-panel--right">
      <p class="certificate-text">TUNING<br>COMPLETED</p>
    </div>
    <p class="shop-name">R7 FORGE</p>
  </div>
</body>
</html>
```